依頼詳細
上記のターゲットに郵送でDMを送り、注文がきたところに飛燕パックを利用して届けるのを考えています。
バナナ1ケース約2500円+運賃
メンバーが多いラグビー部は週4回、馬術部は1回みたいな感じです。
記載項目
社名や連絡先、URL、ロゴなど必要な情報は入れていただつつ、導入事例や注文者に記載していただく表(添付画像参照)なども入れていただきたく存じます。
サイズ
A4
ページ数
両面
希望イメージ
シンプル 複雑
単色 カラフル
暗い 明るい
日常 高級
遊び心 厳粛
未来的 伝統的
女性的 男性的
希望する色
黄 緑
納品ファイル
• 高解像度JPG (.jpg)
• イラストレーター形式 (.ai)

```html
<!DOCTYPE html>
<html lang="ja">
<head>
<meta charset="utf-8">
<title>青葉バナナ便 チラシ 表面</title>
<link rel="stylesheet" href="https://fonts.googleapis.com/css2?family=Yusei+Magic&family=Kosugi+Maru&family=M+PLUS+Rounded+1c:wght@500;800&display=swap">
<style>
  :root{
    --yellow:#f6dc2e;
    --yellow-light:#fbe862;
    --banana-light:#fbe27a;
    --banana-mid:#f4c63a;
    --orange:#ef8a1a;
    --green:#7cc043;
    --green-pale:#eef6e2;
    --green-dark:#4f9a2b;
    --ink:#2b2116;
    --white:#ffffff;
    --gray:#555;
  }
  *{margin:0;padding:0;box-sizing:border-box}
  html,body{width:846px;height:1200px;overflow:hidden;background:var(--white)}
  .flyer{position:relative;width:846px;height:1200px;overflow:hidden;font-family:"Kosugi Maru",sans-serif;color:var(--ink)}
  .hero{position:absolute;left:0;top:0;width:846px;height:880px;
    background:repeating-linear-gradient(90deg,var(--yellow) 0 70px,var(--yellow-light) 70px 140px)}
  .badge-new{position:absolute;left:60px;top:36px;width:140px;height:140px;border-radius:50%;background:var(--white);
    display:flex;align-items:center;justify-content:center;text-align:center;color:var(--green-dark);font-size:17px;line-height:1.5}
  .headline-accent{position:absolute;right:36px;top:70px;font-family:"Yusei Magic",sans-serif;font-size:140px;line-height:1;color:var(--orange);transform:rotate(-4deg);letter-spacing:4px}
  .headline{position:absolute;left:66px;top:230px;font-family:"Yusei Magic",sans-serif;font-size:104px;line-height:1.1;color:var(--ink);font-weight:400}
  .tagline{position:absolute;left:230px;top:500px;font-size:24px;color:var(--ink);transform:rotate(-5deg);letter-spacing:2px}
  .banana-art{position:absolute;left:110px;top:575px;width:626px;height:250px;border-radius:28px;
    background:linear-gradient(160deg,var(--banana-light) 0%,var(--banana-mid) 100%)}
  .service-band{position:absolute;left:0;top:880px;width:846px;height:180px;background:var(--green);
    display:flex;align-items:center;padding-left:56px}
  .service-name{font-family:"M PLUS Rounded 1c",sans-serif;font-weight:800;font-size:88px;line-height:1;color:var(--white);letter-spacing:4px}
  .depart{position:absolute;right:40px;top:-36px;width:136px;height:136px;border-radius:50%;background:var(--white);
    display:flex;align-items:center;justify-content:center;font-family:"Yusei Magic",sans-serif;font-size:42px;color:var(--green-dark)}
  .footer{position:absolute;left:0;top:1060px;width:846px;height:140px;background:var(--green-pale);display:flex;align-items:center;padding:0 44px;gap:36px}
  .company{display:flex;align-items:center;gap:14px;flex-shrink:0}
  .company-mark{width:56px;height:56px;border-radius:50%;background:var(--green)}
  .company-name{font-size:26px;color:var(--green-dark)}
  .contact{font-size:14px;color:var(--gray);line-height:1.9}
  .web-row{display:flex;align-items:center;gap:10px}
  .web-link{font-size:17px;color:var(--green-dark)}
  .search{display:flex}
  .search-box{width:170px;height:24px;border:1px solid #aaa;background:var(--white);font-size:13px;line-height:20px;padding:0 6px;color:var(--gray)}
  .search-btn{height:24px;padding:0 10px;background:var(--green);color:var(--white);font-size:13px;line-height:24px}
</style>
</head>
<body>
<div class="flyer">
  <section class="hero">
    <div class="badge-new">新サービスで<br>一箱お届け<br>します。</div>
    <div class="headline-accent">バナナ</div>
    <h1 class="headline">おいしい<br>届けます！</h1>
    <p class="tagline">もう、他のバナナは食べられな〜い!!</p>
    <div class="banana-art" role="img" aria-label="大きな一本のバナナのイラスト"></div>
  </section>
  <section class="service-band">
    <h2 class="service-name">青葉バナナ便</h2>
    <div class="depart">出発!!</div>
  </section>
  <footer class="footer">
    <div class="company">
      <span class="company-mark"></span>
      <span class="company-name">株式会社 青葉</span>
    </div>
    <div class="contact">
      東京都港区青葉町1丁目2番3号 TEL 03-0000-1234 / FAX 03-0000-5678
      <div class="web-row">
        <span class="web-link">ホームページはこちらから ▶</span>
        <span class="search"><span class="search-box">株式会社 青葉</span><span class="search-btn">検索</span></span>
      </div>
    </div>
  </footer>
</div>
</body>
</html>
```